Office Technology Business Card Design for B2B sales people

I am looking to get a complete redesign of our company business card. It may just be my card that gets updated but I am looking for ideas that will ultimately make me/us proud to leave our business card with prospective and current clients.

The sky is the limit in terms of design. We have two logos to choose from and we must have Quilvor logo on the card somewhere.

I have uploaded a sample of our current card (which I do not like so it is for reference only)

I have also uploaded two logos to play around with.

On the logo that says Performing Daily under the TOE we are going to be removing that phrase and simply putting Tarnwell Office Equipment.

I am looking for both back and Front. Feel free to check out our website and look for content for the back. I am not sure if I want to highlight a few of the more popular solutions that we sell or just leave it with design and no content.

Once again looking for a complete redesign that is Modern, Simple, has a quick "Wow thats impressive" factor when leaving it behind.

www.toenet-example.com

Industry/Entity Type

Business

Contact Information for Business Card

Must Contain Name, Title, Email, Office Phone, Cell Phone, Address, logo, and quilvor log followed by A quilvor Company. This can be anywhere on the card and does not have to in conjunction with company logo.

Requirements
Must have
• Modern Look and communicates information cleary but pops out as impressive card.
Should not have
• very generic template

```html
<!DOCTYPE html>
<html lang="en">
<head>
<meta charset="utf-8">
<title>Tarnwell Office Equipment – Business Card</title>
<link rel="stylesheet" href="https://fonts.googleapis.com/css2?family=Source+Sans+3:wght@400;600;700&display=swap">
<style>
  :root {
    --stage: #212121;
    --card-front: #ececec;
    --brand-blue: #0a5da4;
    --brand-blue-deep: #064f8f;
    --brand-blue-light: #1c6fb8;
    --ink: #3d3d3d;
    --partner-red: #d4202f;
    --white: #ffffff;
  }
  * { margin: 0; padding: 0; box-sizing: border-box; }
  html, body {
    width: 1200px; height: 900px; overflow: hidden;
    background: var(--stage);
    font-family: "Source Sans 3", Arial, sans-serif;
  }
  .canvas { position: relative; width: 1200px; height: 900px; }
  .card {
    position: absolute; top: 170px; width: 347px; height: 561px;
    text-align: center;
  }
  .card--front { left: 259px; background: var(--card-front); }
  .card--back {
    left: 631px; overflow: hidden;
    background: radial-gradient(circle at 50% 50%, var(--brand-blue) 0%, var(--brand-blue) 50%, var(--brand-blue-deep) 62%, var(--brand-blue-light) 63%, var(--brand-blue) 90%);
  }
  .brand-mark { position: absolute; left: 0; right: 0; }
  .brand-mark__dot { display: block; margin: 0 auto; border-radius: 50%; }
  .brand-mark__name { display: block; font-weight: 700; }
  .card--front .brand-mark { top: 62px; }
  .card--front .brand-mark__dot { width: 84px; height: 84px; background: var(--brand-blue); }
  .card--front .brand-mark__name { margin-top: 18px; font-size: 21px; color: var(--brand-blue); }
  .card--back .brand-mark { top: 190px; }
  .card--back .brand-mark__dot { width: 96px; height: 96px; background: var(--white); }
  .card--back .brand-mark__name { margin-top: 22px; font-size: 24px; color: var(--white); }

  .person { position: absolute; top: 280px; left: 0; right: 0; }
  .person__name {
    font-size: 23px; font-weight: 600; letter-spacing: 1px;
    color: var(--brand-blue-deep); text-transform: uppercase; line-height: 1.1;
  }
  .person__title { font-size: 16px; color: var(--ink); }
  .contact { position: absolute; top: 339px; left: 0; right: 0; font-size: 16px; color: var(--ink); line-height: 20px; }
  .contact__label { font-weight: 700; color: var(--brand-blue-deep); }
  .address { position: absolute; top: 408px; left: 0; right: 0; font-size: 16px; color: var(--ink); line-height: 20px; }

  .partner {
    position: absolute; top: 478px; left: 0; right: 0;
    display: flex; align-items: center; justify-content: center; gap: 10px;
  }
  .partner__name { font-size: 30px; font-weight: 600; color: var(--partner-red); }
  .partner__dot { width: 40px; height: 40px; border-radius: 50%; background: var(--partner-red); }
  .partner__tagline { font-size: 16px; font-weight: 700; color: #111; }

  .website {
    position: absolute; top: 506px; left: 0; right: 0;
    font-size: 15px; font-weight: 700; color: var(--white);
  }
</style>
</head>
<body>
<main class="canvas">
  <section class="card card--front" aria-label="Card front">
    <div class="brand-mark">
      <span class="brand-mark__dot"></span>
      <span class="brand-mark__name">Tarnwell Office Equipment</span>
    </div>
    <div class="person">
      <h1 class="person__name">Daniel Harper</h1>
      <p class="person__title">Managing Director</p>
    </div>
    <p class="contact">
      <span class="contact__label">P:</span> 044-123 456 789<br>
      <span class="contact__label">M:</span> 044-123 456 789<br>
      <span class="contact__label">E:</span> info@webname.com
    </p>
    <p class="address">12345, Address Goes Here<br>Country Name, 123456.</p>
    <div class="partner">
      <span class="partner__name">quilvor</span>
      <span class="partner__dot"></span>
      <span class="partner__tagline">A Quilvor Company</span>
    </div>
  </section>

  <section class="card card--back" aria-label="Card back">
    <div class="brand-mark">
      <span class="brand-mark__dot"></span>
      <span class="brand-mark__name">Tarnwell Office Equipment</span>
    </div>
    <p class="website">www.websitename.com</p>
  </section>
</main>
</body>
</html>
```